Magazine advertisement for wedding proposal

SPECS
Page size: 221,0-290,0
File format:Certified PDF PrintSpec_7Q2 (CMYK).
supply with crop marks on sheet mirror format
boundlessly knitted

CONTENT
I am going to ask my wife to marry me (again). I have bought a 1/1 page in her favourite Glossy. I would like the advertisement to present a letter from a type machine covered with some polaroid pictures of her. Idea is to mimic a guy in love writing a letter and dreaming away at her pictures. I would like the whole look and feel to be professional and in style. As such colours etc. may be changed and altered to make it a great integrated piece. I have added multiple pohoto's. Not all have to be used. You can choose which and how much you find most appealing. I At least want Photo Noor 1 to be used and one of the pictures with us together in white (couple).

The letter should read the following text:

Once in your lifetime you meet someone who changes everything.
She is going to do her thing with or without you. That's why she is a queen.

But we are just better together, babe...☺
That's why I want you to love me, stay with me and marry me. Would you?

Fenna,

Wil je met me trouwen?

-xxx-

Wouter

Requirements
Must have
• Be creative! This is just my first thought, but if you have an idea which you think is better, please let me know.
• - light & warm colours which all have the same look and feel (I do not like too much accent and opposite colours)
• - text as a love letter or poem
• - usage of Photo Noor 1
• - usage of couple photo
• - usage of both photo's with kids
Should not have
• - too cliché props - one or two things like hearts and flowers is ok, but dont overdo it

```html
<!DOCTYPE html>
<html lang="en">
<head>
<meta charset="utf-8">
<title>Would You? – Proposal Page</title>
<link rel="stylesheet" href="https://fonts.googleapis.com/css2?family=Bodoni+Moda:wght@400;700&display=swap">
<style>
  :root {
    --butter: #fef39c;
    --rose: #ec2a7b;
    --sky: #a9d8f3;
    --sky-deep: #8cc6ea;
    --ink: #2a2624;
    --paper: #ffffff;
    --skin: #e9c7a8;
    --linen: #f4efe6;
  }
  * { box-sizing: border-box; margin: 0; padding: 0; }
  html, body { width: 915px; height: 1200px; overflow: hidden; background: var(--butter); }
  .page {
    position: relative;
    width: 915px; height: 1200px;
    background: var(--butter);
    font-family: "Bodoni Moda", "Didot", serif;
  }
  .panel {
    position: absolute;
    left: 43px; top: 43px;
    width: 829px; height: 1114px;
    background: var(--rose);
  }
  .crown {
    position: absolute;
    left: 254px; top: 208px;
    width: 54px; height: 34px;
  }
  .letter {
    position: absolute;
    left: 60px; top: 254px;
    width: 440px;
    text-align: center;
    color: var(--paper);
    font-size: 32px;
    line-height: 51.5px;
  }
  .letter strong { font-weight: 700; }
  .letter .queen { letter-spacing: 2px; }
  .heart-photo {
    position: absolute;
    left: 405px; top: 78px;
    width: 492px; height: 442px;
  }
  .polaroid {
    position: absolute;
    background: var(--paper);
    padding: 8px;
    box-shadow: 0 2px 6px rgba(0,0,0,0.18);
  }
  .polaroid .shot {
    width: 100%; height: 100%;
  }
  .polaroid--beach {
    left: 574px; top: 568px;
    width: 140px; height: 138px;
    transform: rotate(-17deg);
  }
  .polaroid--beach .shot { background: linear-gradient(160deg, #d9cfc2, #f1e6d6 55%, #c9b7a3); }
  .polaroid--hug {
    left: 650px; top: 742px;
    width: 140px; height: 136px;
    transform: rotate(11deg);
  }
  .polaroid--hug .shot { background: linear-gradient(200deg, #cfe0ea, #f0dcc4 55%, #d8b996); }
  .couple-photo {
    position: absolute;
    left: 339px; top: 705px;
    width: 244px; height: 452px;
    border-radius: 110px 110px 0 0;
    background: linear-gradient(180deg, #c99866 0%, var(--skin) 22%, var(--linen) 45%, #fbfaf7 100%);
  }
  .closing {
    position: absolute;
    left: 0; top: 0;
    width: 915px;
    color: var(--ink);
    font-size: 37px;
  }
  .closing .band {
    position: absolute;
    height: 44px;
    line-height: 44px;
    background: var(--butter);
    text-align: center;
    white-space: nowrap;
  }
  .band--one   { left: 102px; top: 949px;  width: 752px; }
  .band--two   { left: 43px;  top: 1001px; width: 748px; padding-left: 40px; }
  .band--three { left: 181px; top: 1057px; width: 691px; text-align: left; padding-left: 18px; }
  .band--ask   { left: 264px; top: 1113px; width: 379px; font-weight: 700; letter-spacing: 1px; }
</style>
</head>
<body>
<main class="page">
  <div class="panel"></div>

  <svg class="heart-photo" viewBox="0 0 492 442" role="img" aria-label="Portrait photo of a smiling blonde woman set inside a brushed heart shape">
    <defs>
      <linearGradient id="heartFill" x1="0" y1="0" x2="1" y2="1">
        <stop offset="0" stop-color="#b8e0f7"/>
        <stop offset="0.45" stop-color="#e6cdb4"/>
        <stop offset="0.7" stop-color="#d9b08c"/>
        <stop offset="1" stop-color="#8cc6ea"/>
      </linearGradient>
    </defs>
    <path d="M246 62 C214 8 140 -6 86 16 C20 44 -6 120 20 190 C48 262 140 340 150 402 L160 440 C210 380 330 318 410 246 C478 186 500 110 470 56 C440 4 360 -6 300 20 C276 30 258 44 246 62 Z" fill="url(#heartFill)"/>
  </svg>

  <svg class="crown" viewBox="0 0 54 34" aria-hidden="true">
    <path d="M4 10 L14 22 L27 4 L40 22 L50 10 L46 28 L8 28 Z" fill="none" stroke="#ffffff" stroke-width="2" stroke-linejoin="round"/>
    <line x1="9" y1="32" x2="45" y2="32" stroke="#ffffff" stroke-width="2"/>
  </svg>

  <p class="letter">
    Once in your<br>
    lifetime you meet<br>
    someone who changes<br>
    <strong>EVERYTHING.</strong><br>
    She is going to do her<br>
    thing with or<br>
    <strong>WITHOUT YOU.</strong><br>
    That's why she is a<br>
    <span class="queen">QUEEN.</span>
  </p>

  <figure class="polaroid polaroid--beach">
    <div class="shot" role="img" aria-label="Snapshot of mother in sunglasses with a laughing toddler in a sun hat"></div>
  </figure>
  <figure class="polaroid polaroid--hug">
    <div class="shot" role="img" aria-label="Snapshot of mother hugging a smiling blond boy"></div>
  </figure>

  <div class="couple-photo" role="img" aria-label="Photo of the couple dressed in white, embracing"></div>

  <div class="closing">
    <p class="band band--one">But we are just better together, babe</p>
    <p class="band band--two">That's why I want you to love me,</p>
    <p class="band band--three">stay with me and marry me.</p>
    <p class="band band--ask">WOULD YOU?</p>
  </div>
</main>
</body>
</html>
```